Tarn’s Beauty. Coffee Scrub Skincare

Graphic design for my Coffee Scrub skin care business. Tarn’s Beauty. To go on the packaging. Fun with pastel colours, but still clean and professional. See attached photos on similar businesses packaging. I like the “Bree & Ula” font (see attached photo).

Things to write on the packaging: Tarn’s Beauty. Recycled Coffee scrub. Coconut and Chocolate. Recycled packaging. Vegan. Not tested on animal. Recycled coffee. Pink Australian clay. 150g 5.29 oz. Made in Australia.

```html
<!DOCTYPE html>
<html lang="en">
<head>
<meta charset="utf-8">
<title>Tarn’s Beauty – Chocolate Coffee Scrub Pouch</title>
<link rel="stylesheet" href="https://fonts.googleapis.com/css2?family=Nunito+Sans:wght@400;600;700&display=swap">
<style>
  :root {
    --backdrop: #d4d5d9;
    --pouch-brown: #7a4b26;
    --pouch-brown-light: #8a5a33;
    --pouch-brown-dark: #6a3f1f;
    --band-brown: #3b2417;
    --cream: #e8dfcf;
    --ink-dark: #3a2518;
    --band-text: #a8794f;
    --pattern-tone: rgba(214, 170, 130, 0.18);
  }
  * { box-sizing: border-box; margin: 0; padding: 0; }
  html, body {
    width: 927px;
    height: 1200px;
    overflow: hidden;
    background: var(--backdrop);
    font-family: "Nunito Sans", sans-serif;
  }
  .canvas {
    position: relative;
    width: 927px;
    height: 1200px;
  }
  .pouch {
    position: absolute;
    left: 210px;
    top: 176px;
    width: 530px;
    height: 862px;
    background: linear-gradient(100deg, var(--pouch-brown-dark) 0%, var(--pouch-brown) 35%, var(--pouch-brown-light) 55%, var(--pouch-brown) 75%, var(--pouch-brown-dark) 100%);
    overflow: hidden;
    text-align: center;
  }
  .pattern-area {
    position: absolute;
    background: var(--pattern-tone);
    border-radius: 50%;
    filter: blur(14px);
  }
  .pattern-area--top-right { right: -40px; top: 60px; width: 150px; height: 340px; }
  .pattern-area--bottom-left { left: -40px; top: 470px; width: 150px; height: 300px; }
  .pattern-area--top-left { left: 0; top: 0; width: 110px; height: 40px; }
  .brand-name {
    position: absolute;
    top: 62px;
    left: 0;
    right: 0;
    font-weight: 700;
    font-size: 21px;
    letter-spacing: 0.22em;
    color: var(--ink-dark);
    text-transform: uppercase;
  }
  .brand-mark {
    position: absolute;
    top: 250px;
    left: 0;
    right: 0;
    display: flex;
    justify-content: center;
    align-items: center;
    gap: 14px;
  }
  .brand-mark__dot {
    width: 22px;
    height: 22px;
    border-radius: 50%;
    background: var(--cream);
  }
  .brand-mark__name {
    font-weight: 700;
    font-size: 44px;
    color: var(--cream);
    letter-spacing: 0.04em;
  }
  .product-flavour {
    position: absolute;
    top: 374px;
    left: 0;
    right: 0;
    font-weight: 600;
    font-size: 36px;
    letter-spacing: 0.24em;
    color: var(--cream);
    padding-left: 0.24em;
  }
  .product-type {
    position: absolute;
    top: 415px;
    left: 0;
    right: 0;
    font-weight: 700;
    font-size: 16px;
    letter-spacing: 0.06em;
    color: var(--cream);
  }
  .ingredients {
    position: absolute;
    top: 515px;
    left: 0;
    right: 0;
    font-weight: 700;
    font-size: 17px;
    line-height: 28px;
    letter-spacing: 0.05em;
    color: var(--cream);
    list-style: none;
  }
  .origin {
    position: absolute;
    top: 660px;
    left: 0;
    right: 0;
    color: var(--ink-dark);
  }
  .origin__country { font-weight: 400; font-size: 17px; line-height: 22px; }
  .origin__claims { font-weight: 400; font-size: 16px; line-height: 22px; opacity: 0.75; }
  .base-band {
    position: absolute;
    left: 0;
    right: 0;
    bottom: 0;
    height: 116px;
    background: var(--band-brown);
    color: var(--band-text);
    padding-top: 30px;
    font-size: 16px;
    line-height: 24px;
  }
</style>
</head>
<body>
<main class="canvas">
  <section class="pouch">
    <div class="pattern-area pattern-area--top-left" role="img" aria-label="Decorative dot pattern"></div>
    <div class="pattern-area pattern-area--top-right" role="img" aria-label="Decorative dot and brush-stroke pattern"></div>
    <div class="pattern-area pattern-area--bottom-left" role="img" aria-label="Decorative dot and brush-stroke pattern"></div>

    <p class="brand-name">Tarn’s Beauty</p>

    <div class="brand-mark">
      <span class="brand-mark__dot"></span>
      <span class="brand-mark__name">Tarn’s</span>
    </div>

    <h1 class="product-flavour">CHOCOLATE</h1>
    <p class="product-type">COFFEE SCRUB</p>

    <ul class="ingredients">
      <li>RECYCLED COFFEE</li>
      <li>PINK AUSTRALIAN CLAY</li>
    </ul>

    <div class="origin">
      <p class="origin__country">MADE IN AUSTRALIA</p>
      <p class="origin__claims">Vegan. Not tested on animals.</p>
    </div>

    <footer class="base-band">
      <p>Recycled Packaging</p>
      <p>150g 5.29oz</p>
    </footer>
  </section>
</main>
</body>
</html>
```